Quiet Fern Acupuncture
Quiet Fern Acupuncture -
Creative Brief
Bright & Fun-filled
Marla Pennick-Vasquez
LAc, Dipl, Ac
2730 N Ridley Avenue, Suite 410 Larkmoor, AZ, 86044 @ Haverstock Chiropractic
quietfernacupuncture@mailbox-example.com
an appointment reminder card

```html
<!DOCTYPE html>
<html lang="en">
<head>
<meta charset="utf-8">
<title>Quiet Fern Acupuncture – Stationery Set</title>
<link rel="stylesheet" href="https://fonts.googleapis.com/css2?family=Open+Sans:wght@400;600;700&display=swap">
<style>
  :root{
    --backdrop:#e9e4dc;
    --paper:#ffffff;
    --ink:#333333;
    --muted:#777777;
    --rule:#9a9a9a;
    --orange:#f07a12;
    --amber:#fbb03b;
    --deep:#d9480f;
    --black:#111111;
    --label:#2b2b2b;
  }
  *{box-sizing:border-box;margin:0;padding:0}
  html,body{width:1200px;height:562px;overflow:hidden}
  body{background:var(--backdrop);font-family:"Open Sans",Arial,sans-serif;color:var(--ink);position:relative}
  .piece{position:absolute;background:var(--paper);box-shadow:0 2px 6px rgba(0,0,0,.25);overflow:hidden}
  .piece-label{position:absolute;font-size:7px;font-weight:700;color:var(--label);text-align:center;width:100%;top:-11px;left:0}
  .labelled{overflow:visible}
  .swoosh{position:absolute;inset:0;width:100%;height:100%;pointer-events:none}
  .brand{position:absolute;font-weight:700;color:var(--deep);line-height:1.05}
  .brand-dot{position:absolute;border-radius:50%;background:radial-gradient(circle at 40% 40%,var(--amber),var(--orange) 70%,var(--deep))}
  .faint-art{position:absolute;border-radius:50%;background:radial-gradient(ellipse at center,rgba(240,122,18,.14),rgba(150,160,210,.12) 55%,rgba(255,255,255,0) 75%)}
  .footer{position:absolute;left:0;right:0;text-align:center;font-size:4.5px;color:var(--muted);line-height:1.4}

  /* fax cover */
  .fax{left:58px;top:28px;width:314px;height:520px}
  .fax-title{position:absolute;right:24px;top:54px;font-size:9px;font-weight:700;color:var(--ink)}
  .fax-table{position:absolute;left:26px;top:70px;width:264px;border-collapse:collapse;font-size:5px}
  .fax-table td{border:1px solid var(--rule);height:17px;padding:2px 3px;vertical-align:top;width:25%}
  .fax-checks{position:absolute;left:26px;top:168px;display:flex;gap:14px;font-size:5px}
  .fax-checks span::before{content:"";display:inline-block;width:5px;height:5px;border:1px solid var(--rule);margin-right:3px;vertical-align:-1px}
  .fax-lines{position:absolute;left:26px;right:24px;top:186px;height:1px;background:var(--rule)}

  /* letterhead */
  .letterhead{left:408px;top:28px;width:302px;height:520px}

  /* business cards */
  .card-front{left:742px;top:36px;width:156px;height:112px}
  .card-back{left:918px;top:36px;width:258px;height:112px}
  .card-contact{position:absolute;left:70px;top:42px;font-size:4.5px;line-height:1.5;color:var(--ink)}
  .card-contact strong{font-size:5.5px;font-weight:700;display:block}
  .reminder{position:absolute;left:16px;top:62px;right:16px;font-size:5px}
  .reminder-title{font-weight:700;margin-bottom:6px}
  .reminder-row{display:flex;gap:12px}
  .reminder-row span{flex:1;border-bottom:1px solid var(--rule);padding-bottom:2px}

  /* envelopes */
  .env-front{left:742px;top:170px;width:434px;height:182px}
  .env-back{left:742px;top:376px;width:434px;height:172px}
  .return-address{position:absolute;left:22px;top:92px;font-size:4.5px;line-height:1.5;color:var(--ink)}
</style>
</head>
<body>

<!-- Fax cover -->
<section class="piece fax labelled">
  <div class="piece-label">Fax Cover</div>
  <svg class="swoosh" viewBox="0 0 314 520" preserveAspectRatio="none" aria-hidden="true">
    <defs><linearGradient id="warm" x1="0" y1="0" x2="1" y2="1"><stop offset="0" stop-color="#fbb03b"/><stop offset="1" stop-color="#e85d0c"/></linearGradient></defs>
    <path d="M262 0 Q300 25 314 80 L314 0 Z" fill="url(#warm)"/>
    <path d="M252 0 Q296 28 314 92 L314 80 Q300 25 262 0 Z" fill="#111"/>
    <path d="M0 445 Q20 500 64 520 L0 520 Z" fill="url(#warm)"/>
    <path d="M0 433 Q18 500 76 520 L64 520 Q20 500 0 445 Z" fill="#111"/>
  </svg>
  <div class="brand-dot" style="left:26px;top:24px;width:12px;height:12px"></div>
  <div class="brand" style="left:42px;top:24px;font-size:8px">Quiet Fern<br>Acupuncture</div>
  <div class="fax-title">FAX</div>
  <table class="fax-table">
    <tr><td>To:</td><td></td><td>From:</td><td></td></tr>
    <tr><td>Fax:</td><td></td><td>Pages:</td><td></td></tr>
    <tr><td>Phone:</td><td></td><td>Date:</td><td></td></tr>
    <tr><td>Re:</td><td></td><td>CC:</td><td></td></tr>
  </table>
  <div class="fax-checks"><span>Urgent</span><span>For Review</span><span>Please Comment</span><span>Please Reply</span><span>Please Recycle</span></div>
  <div class="fax-lines"></div>
  <div class="faint-art" role="img" aria-label="Faint decorative birds on curling branches" style="left:70px;top:250px;width:200px;height:170px"></div>
  <div class="footer" style="bottom:14px">2730 N Ridley Avenue, Suite 410 Larkmoor, AZ 86044<br>T: (928) 555-0147 &nbsp; E: quietfernacupuncture@mailbox-example.com</div>
</section>

<!-- Letterhead -->
<section class="piece letterhead labelled">
  <div class="piece-label">Letterhead</div>
  <svg class="swoosh" viewBox="0 0 302 520" preserveAspectRatio="none" aria-hidden="true">
    <defs><linearGradient id="warm2" x1="0" y1="0" x2="1" y2="1"><stop offset="0" stop-color="#fbb03b"/><stop offset="1" stop-color="#e85d0c"/></linearGradient></defs>
    <path d="M250 0 Q288 25 302 80 L302 0 Z" fill="url(#warm2)"/>
    <path d="M240 0 Q284 28 302 92 L302 80 Q288 25 250 0 Z" fill="#111"/>
    <path d="M0 445 Q20 500 64 520 L0 520 Z" fill="url(#warm2)"/>
    <path d="M0 433 Q18 500 76 520 L64 520 Q20 500 0 445 Z" fill="#111"/>
  </svg>
  <div class="brand-dot" style="left:112px;top:30px;width:14px;height:14px"></div>
  <div class="brand" style="left:130px;top:30px;font-size:8px">Quiet Fern<br>Acupuncture</div>
  <div class="faint-art" role="img" aria-label="Faint decorative birds on curling branches" style="left:50px;top:230px;width:210px;height:180px"></div>
  <div class="footer" style="bottom:14px">2730 N Ridley Avenue, Suite 410 Larkmoor, AZ 86044<br>T: (928) 555-0147 &nbsp; E: quietfernacupuncture@mailbox-example.com</div>
</section>

<!-- Business card front -->
<section class="piece card-front labelled">
  <div class="piece-label">Business Card (Front)</div>
  <svg class="swoosh" viewBox="0 0 156 112" preserveAspectRatio="none" aria-hidden="true">
    <defs><linearGradient id="warm3" x1="0" y1="0" x2="1" y2="1"><stop offset="0" stop-color="#fbb03b"/><stop offset="1" stop-color="#e85d0c"/></linearGradient></defs>
    <path d="M0 0 L52 0 Q34 50 48 112 L0 112 Z" fill="url(#warm3)"/>
    <path d="M52 0 L56 0 Q38 50 52 112 L48 112 Q34 50 52 0 Z" fill="#111"/>
  </svg>
  <div class="brand-dot" style="left:12px;top:40px;width:28px;height:28px"></div>
  <div class="card-contact">
    <strong>Marla Pennick-Vasquez</strong>
    LAc, Dipl, Ac<br>
    2730 N Ridley Avenue, Suite 410<br>
    Larkmoor, AZ, 86044<br>
    T: (928) 555-0147
  </div>
</section>

<!-- Business card back -->
<section class="piece card-back labelled">
  <div class="piece-label">Business Card (Back)</div>
  <div class="brand-dot" style="left:119px;top:12px;width:20px;height:20px"></div>
  <div class="brand" style="left:0;right:0;top:36px;font-size:7px;text-align:center">Quiet Fern Acupuncture</div>
  <div class="reminder">
    <div class="reminder-title">Your next appointment</div>
    <div class="reminder-row"><span>Day</span><span>Date</span><span>Time</span><span>Date</span><span>Time</span></div>
  </div>
</section>

<!-- Envelope front -->
<section class="piece env-front labelled">
  <div class="piece-label">Envelope (Front)</div>
  <svg class="swoosh" viewBox="0 0 434 182" preserveAspectRatio="none" aria-hidden="true">
    <defs><linearGradient id="warm4" x1="0" y1="0" x2="1" y2="1"><stop offset="0" stop-color="#fbb03b"/><stop offset="1" stop-color="#e85d0c"/></linearGradient></defs>
    <path d="M350 0 Q410 20 434 70 L434 0 Z" fill="url(#warm4)"/>
    <path d="M336 0 Q404 22 434 84 L434 70 Q410 20 350 0 Z" fill="#111"/>
    <path d="M434 130 Q410 170 370 182 L434 182 Z" fill="url(#warm4)"/>
  </svg>
  <div class="brand-dot" style="left:24px;top:16px;width:40px;height:40px"></div>
  <div class="brand" style="left:22px;top:62px;font-size:7px">Quiet Fern Acupuncture</div>
  <div class="return-address">2730 N Ridley Avenue, Suite 410<br>Larkmoor, AZ, 86044</div>
  <div class="faint-art" role="img" aria-label="Faint decorative birds on curling branches" style="left:40px;top:90px;width:120px;height:90px;opacity:.6"></div>
</section>

<!-- Envelope back -->
<section class="piece env-back labelled">
  <div class="piece-label">Envelope (Back)</div>
  <svg class="swoosh" viewBox="0 0 434 172" preserveAspectRatio="none" aria-hidden="true">
    <path d="M0 0 L217 70 L434 0" fill="#f6f6f6" stroke="#c8c8c8" stroke-width="1"/>
    <path d="M0 172 L170 80 M434 172 L264 80" fill="none" stroke="#d8d8d8" stroke-width="1"/>
  </svg>
  <div class="brand-dot" style="left:200px;top:54px;width:34px;height:34px"></div>
</section>

</body>
</html>
```